Re-design of 4 x 2-sided reports

I need the 4 attached reports (3 are 2-sides of A4; 1 is 7-sides of A4) to be re-designed with a consistent look and feel. Just need 1 or 2 images per report being inserted plus consistent branding and contact details being displayed in the same location on each report with same colour, font and design). Reports are attached.
The reports are used as lead magnets.
That is, visitors to our website can download one of them (7 Steps To Sharpen Your Sales Over The Coming Month) by filling in a form with their email address. Then over the next 30 days the other reports are sent to the subscriber via email autoresponders.
Blue Harbour Marketing is a marketing consultancy dealing with companies in the North West of England providing cost-effective and profitable marketing to small and medium-sized businesses that want better and quicker results. The reports need to be professional and corporate looking. Please let me know if you need any further clarification or have any questions. I attach an example report. I don't necessarily want to mirror this report (from the law firm) but it may help to understand what look I'm trying to get. Many thanks, Gordon

Target Market(s)

SMEs based in NW of England
Typically with turnover of £1m to £10m or 10 to 100 employees
Clients often in the construction sector, healthcare, accountants, lawyers and local councils.

Industry/Entity Type

Marketing

Font styles to use
Serif
Sans Serif

Colors
ec1f27

Requirements
Must have
• Consistent branding
• Logo in same place across all four reports
• Contact details in same place across all four reports
• Same font across all four reports
• Same colour across all four reports
• Professional and bold look
Nice to have
• Some strong stock photography
• 1 or 2 images per report
• More images for the 7-page report though
Should not have
• No graphics

```html
<!DOCTYPE html>
<html lang="en">
<head>
<meta charset="utf-8">
<title>7 Steps To Sharpen Your Sales Over The Coming Month – Blue Harbour Marketing</title>
<link rel="stylesheet" href="https://fonts.googleapis.com/css2?family=Oswald:wght@500;600&family=Carlito:wght@400;700&family=Ubuntu:wght@300;500&display=swap">
<style>
:root{
  --red:#e31e26;
  --maroon:#7d1a22;
  --ink:#1e1e1e;
  --copy:#444;
  --bar:#e6e6e6;
  --backdrop:#dfe0e2;
  --paper:#ffffff;
}
*{margin:0;padding:0;box-sizing:border-box}
html,body{width:1200px;height:848px;overflow:hidden;background:var(--backdrop)}
.sheet{position:absolute;top:50px;width:524px;height:734px;background:var(--paper);overflow:hidden;font-family:"Carlito",sans-serif}
.sheet--front{left:61px}
.sheet--back{left:614px}
.hero{position:absolute;left:0;top:0;display:block}
.headline{position:absolute;left:19px;top:164px;font-family:"Oswald",sans-serif;color:var(--ink);line-height:1.05}
.headline__big{display:block;font-size:52px;font-weight:600;color:var(--red);letter-spacing:.5px;line-height:1}
.headline__line{display:block;font-size:17px;font-weight:500}
.headline__line--accent{color:var(--red);font-size:20px}
.step{position:absolute}
.step__bar{height:21px;background:var(--bar);border:1.5px solid #f08a8e;border-left:none;display:flex;align-items:center;padding-left:20px;font-size:12px;font-weight:700;color:var(--ink);white-space:nowrap}
.step__num{color:var(--red);margin-right:4px}
.step__body{font-size:6.6px;line-height:1.42;color:var(--copy);text-align:justify;margin-top:9px}
.step__list{display:grid;grid-template-columns:150px 150px;gap:2px 10px;margin-top:12px;font-size:6.6px;color:var(--copy)}
.step__list b{color:var(--red);font-weight:400}
.brand{position:absolute;text-align:center;font-family:"Ubuntu",sans-serif;font-weight:500;color:var(--maroon)}
.brand__mark{display:block;margin:0 auto;background:var(--maroon)}
.cta{position:absolute;font-family:"Ubuntu",sans-serif}
.cta__label{display:block;color:var(--red);font-weight:500;font-size:34px;letter-spacing:-.5px;line-height:1}
.cta__phone{display:block;color:var(--ink);font-weight:300;font-size:34px;line-height:1;margin-top:8px}
.band{position:absolute;left:0;width:100%;color:#fff;text-align:center;font-family:"Carlito",sans-serif;display:flex;align-items:center;justify-content:center}
.band--email{background:var(--maroon);font-size:13px}
.band--web{background:var(--red);font-size:12px;font-weight:700;letter-spacing:4px}
</style>
</head>
<body>

<!-- Page one -->
<section class="sheet sheet--front">
  <svg class="hero" width="524" height="300" viewBox="0 0 524 300">
    <defs>
      <linearGradient id="teamTone" x1="0" y1="0" x2="1" y2="1">
        <stop offset="0" stop-color="#4b4a4e"/>
        <stop offset=".5" stop-color="#c9b8a8"/>
        <stop offset="1" stop-color="#8c9fb5"/>
      </linearGradient>
      <linearGradient id="swoosh" x1="0" y1="0" x2="1" y2="0">
        <stop offset="0" stop-color="#e31e26"/>
        <stop offset="1" stop-color="#a3151c"/>
      </linearGradient>
    </defs>
    <path role="img" aria-label="Photo of a smiling business team in suits" fill="url(#teamTone)"
      d="M0 0H524V245C470 240 420 220 360 190C250 140 120 112 0 128Z"/>
    <path fill="url(#swoosh)" d="M0 126C120 110 250 138 370 194C430 222 480 240 524 244V292C470 286 420 266 360 236C250 182 120 146 0 150Z"/>
    <path fill="none" stroke="#fff" stroke-width="3" d="M0 138C120 122 250 152 370 208C430 236 480 256 524 262"/>
    <path fill="none" stroke="#7d1a22" stroke-width="1.5" d="M0 146C120 134 250 164 370 220C430 248 480 268 524 276"/>
  </svg>

  <h1 class="headline">
    <span class="headline__big">7 Steps</span>
    <span class="headline__line">To Sharpen</span>
    <span class="headline__line headline__line--accent">Your Sales</span>
    <span class="headline__line">Over The Coming Month</span>
  </h1>

  <article class="step" style="left:0;top:306px;width:271px">
    <h2 class="step__bar"><span class="step__num">1.</span>Review your existing customer database -</h2>
    <p class="step__body" style="padding:0 8px 0 24px">Can you cross sell other products or services to them? It's much cheaper to sell to your existing customers than try to find new customers. Can you upsell them i.e. to encourage them to purchase either more products, or products on a more frequent basis, or products of a greater total value?</p>
  </article>

  <article class="step" style="left:283px;top:306px;width:241px">
    <h2 class="step__bar" style="border-left:1.5px solid #f08a8e;padding-left:8px"><span class="step__num">3.</span>Get a marketing plan -</h2>
    <p class="step__body" style="padding:0 12px 0 8px">A list of marketing activity that can be undertaken month-by-month for 12 months. You will be amazed at how quickly you will reach the goals for your business with a marketing plan!</p>
  </article>

  <article class="step" style="left:0;top:408px;width:271px">
    <h2 class="step__bar"><span class="step__num">2.</span>Review your value proposition -</h2>
    <p class="step__body" style="padding:0 8px 0 24px;font-size:5.6px">i.e. what value do you offer your customers? List all the benefits of your products, services and your business offers customers and how these differ from your competitors. Put these benefits in your sales and corporate literature, on your website and in your social media profiles. Make sure your sales team knows these benefits by heart!</p>
  </article>

  <article class="step" style="left:283px;top:408px;width:241px">
    <h2 class="step__bar" style="border-left:1.5px solid #f08a8e;padding-left:8px"><span class="step__num">4.</span>Optimise your website -</h2>
    <p class="step__body" style="padding:0 12px 0 8px">To increase the number of visitors to it, in order to increase the probability that people will engage with your business and eventually become customers</p>
  </article>

  <article class="step" style="left:0;top:506px;width:271px">
    <h2 class="step__bar"><span class="step__num">4.</span>Optimise your website -</h2>
    <p class="step__body" style="padding:0 8px 0 24px;font-size:5.6px">More people now search the internet via their mobile phone or tablet than a PC or laptop! Research shows that consumers are more likely to buy from a business with a mobile friendly website than one that only has a standard website</p>
  </article>

  <div class="cta" style="left:31px;top:584px">
    <span class="cta__label">CALL US NOW</span>
    <span class="cta__phone">01632 960 415</span>
  </div>

  <div class="brand" style="left:352px;top:512px;width:124px">
    <span class="brand__mark" style="width:86px;height:86px"></span>
    <span style="display:block;font-size:13px;line-height:1.15;margin-top:6px">Blue Harbour Marketing</span>
  </div>

  <div class="band band--email" style="top:670px;height:30px">info@blueharbourmarketing.co.uk</div>
  <div class="band band--web" style="top:700px;height:34px">www.blueharbourmarketing.co.uk</div>
</section>

<!-- Page two -->
<section class="sheet sheet--back">
  <svg class="hero" width="524" height="230" viewBox="0 0 524 230">
    <defs>
      <linearGradient id="officeTone" x1="0" y1="0" x2="1" y2="0">
        <stop offset="0" stop-color="#b9c2c9"/>
        <stop offset=".55" stop-color="#e6e2df"/>
        <stop offset="1" stop-color="#ffffff"/>
      </linearGradient>
      <linearGradient id="swooshBack" x1="0" y1="0" x2="1" y2="1">
        <stop offset="0" stop-color="#a3151c"/>
        <stop offset=".6" stop-color="#e31e26"/>
        <stop offset="1" stop-color="#ef3a40"/>
      </linearGradient>
    </defs>
    <rect role="img" aria-label="Photo of colleagues reviewing work on a laptop in a bright office" x="0" y="0" width="524" height="192" fill="url(#officeTone)"/>
    <path fill="url(#swooshBack)" d="M250 0H524V208C470 160 420 110 360 72C320 46 285 20 250 0Z"/>
    <path fill="#fff" d="M300 0C360 30 420 80 470 140C490 165 508 190 524 212V232C500 200 470 170 430 140C380 100 320 40 280 0Z"/>
    <path fill="var(--red)" d="M280 0C330 44 390 96 440 140C470 166 500 196 524 222V230C498 204 466 178 436 152C380 104 320 46 266 0Z"/>
  </svg>

  <article class="step" style="left:0;top:203px;width:524px">
    <h2 class="step__bar" style="width:184px;padding-left:26px"><span class="step__num">6.</span>Embrace social media -</h2>
    <p class="step__body" style="padding:0 26px">it's here to stay and those businesses, even small and medium-sized businesses, that choose to ignore social media will be left behind in the near future</p>
    <div class="step__list" style="padding-left:26px">
      <span><b>a.</b> Set up a Friendwall Page (not profile)</span>
      <span><b>d.</b> Set up a ProNetwork Company Profile</span>
      <span><b>b.</b> Set up a Searchly Plus Page</span>
      <span><b>e.</b> Start to use all of the above</span>
      <span><b>c.</b> Set up a company Chirper account</span>
    </div>
  </article>

  <article class="step" style="left:0;top:306px;width:524px">
    <h2 class="step__bar" style="width:178px;padding-left:26px"><span class="step__num">7.</span>Image is all -</h2>
    <p class="step__body" style="padding:0 26px">get your branding, corporate literature, sales literature, exhibition materials and website reviewed - professionally - and re-designed to be congruent with who you are as a company and how you want to position your company in the minds of your existing customers and potential customers</p>
  </article>

  <article class="step" style="left:0;top:374px;width:524px">
    <h2 class="step__bar" style="width:288px;padding-left:26px"><span class="step__num">8.</span>Explore video marketing -</h2>
    <p class="step__body" style="padding:0 26px">the number of videos watched on Streamview and other video channels such as Reelhub will blow your mind. The benefits of video marketing are massive: more traffic to your website, higher profile and awareness of your business, greater credibility and authority, and the biggest, free way to expose your business to your existing and potential customers there is, bar none!</p>
  </article>

  <article class="step" style="left:0;top:444px;width:524px">
    <h2 class="step__bar" style="width:308px;padding-left:26px"><span class="step__num">9.</span>If you don't sell via the internet, you should -</h2>
    <p class="step__body" style="padding:0 26px">Virtually all businesses can benefit massively from a 'shop on the internet'. Initially, some businesses start via Bidmart or Swapboard but eventually need their own e-commerce website.</p>
  </article>

  <article class="step" style="left:0;top:505px;width:524px">
    <h2 class="step__bar" style="width:478px;padding-left:22px"><span class="step__num">10.</span>Commit to investing time and some resources into regular marketing activity -</h2>
    <p class="step__body" style="padding:0 26px">preferably from a marketing plan. Generally, it's quicker, easier and far more affordable to outsource your marketing than employ someone in-house, at least initially. You will be surprised how quickly regular, focused marketing brings results.</p>
  </article>

  <div class="cta" style="left:34px;top:580px">
    <span class="cta__label">CALL US NOW</span>
    <span class="cta__phone">01632 960 415</span>
  </div>

  <div class="brand" style="left:396px;top:572px;width:96px">
    <span class="brand__mark" style="width:64px;height:64px"></span>
    <span style="display:block;font-size:10px;line-height:1.15;margin-top:4px">Blue Harbour Marketing</span>
  </div>

  <div class="band band--email" style="top:666px;height:28px">info@blueharbourmarketing.co.uk</div>
  <div class="band band--web" style="top:698px;height:36px">www.blueharbourmarketing.co.uk</div>
</section>

</body>
</html>
```